Fashion Design Business Card

I need a new business card designed for a new fashion company. I have attached what I have currently designed. I want it more feminine looking, the logo needs to be gold. I want it simple, feminine and stylish. Please give me some different ideas with the fonts.

I need to send the design we currently have, as we have worked out the logo.
You also need all of our details
Fashion

```html
<!DOCTYPE html>
<html lang="en">
<head>
<meta charset="utf-8">
<title>Marisa Kellan – Business Card</title>
<link rel="stylesheet" href="https://fonts.googleapis.com/css2?family=Cinzel:wght@400;500&family=Cormorant+Garamond:wght@400;500&display=swap">
<style>
  :root {
    --backdrop-top: #b9b7b9;
    --backdrop-mid: #dedede;
    --backdrop-low: #cfcfcf;
    --card-light: #f4f4f4;
    --card-light-edge: #e6e6e6;
    --card-dark-a: #141414;
    --card-dark-b: #5c5c5c;
    --silver: #9a9a9a;
    --silver-dark: #6f6f6f;
    --ink: #2a2a2a;
    --type-grey: #8a8a8a;
    --type-light: #e9e9e9;
    --label: #1e1e1e;
  }
  * { margin: 0; padding: 0; box-sizing: border-box; }
  html, body { width: 1200px; height: 1058px; overflow: hidden; }
  body {
    position: relative;
    background: radial-gradient(ellipse at 50% 75%, var(--backdrop-mid) 0%, var(--backdrop-low) 45%, var(--backdrop-top) 100%);
    font-family: "Cormorant Garamond", Georgia, serif;
  }
  .card {
    position: absolute;
    width: 570px;
    height: 342px;
    border-radius: 14px;
    overflow: hidden;
    box-shadow: 0 14px 18px rgba(0,0,0,0.45);
  }
  .card--back  { left: 313px; top: 49px;  background: linear-gradient(160deg, #ffffff 0%, var(--card-light) 55%, var(--card-light-edge) 100%); }
  .card--front-a { left: 18px; top: 465px; background: linear-gradient(160deg, #fafafa 0%, var(--card-light) 60%, var(--card-light-edge) 100%); }
  .card--front-b { left: 612px; top: 465px; background: radial-gradient(ellipse at 10% 40%, var(--card-dark-a) 0%, #2a2a2a 40%, var(--card-dark-b) 100%); }

  .back__decor {
    position: absolute;
    right: -120px; top: -20px;
    width: 300px; height: 300px;
  }
  .back__brand {
    position: absolute;
    left: 48px; top: 58px;
    display: flex; align-items: center; gap: 22px;
  }
  .back__brand-text { display: flex; flex-direction: column; }
  .back__name {
    font-family: "Cinzel", "Times New Roman", serif;
    font-size: 17px; letter-spacing: 3.4px;
    color: var(--ink);
    opacity: 0.75;
  }
  .back__role {
    font-size: 15px; letter-spacing: 5.2px;
    color: var(--type-grey);
    margin-top: -3px;
  }
  .contact {
    position: absolute;
    left: 72px; top: 242px;
    display: grid;
    grid-template-columns: 80px auto;
    row-gap: 1px;
    font-size: 13.5px;
    letter-spacing: 2.6px;
    color: #555;
  }
  .contact dt { font-family: "Cinzel", serif; font-size: 12px; letter-spacing: 2px; line-height: 16px; }
  .contact dd { line-height: 16px; }

  .front__mark {
    position: absolute;
    left: 50%; top: 34px;
    transform: translateX(-50%);
  }
  .front__name {
    position: absolute;
    left: 0; right: 0; top: 244px;
    text-align: center;
    font-family: "Cinzel", "Times New Roman", serif;
    font-size: 27px;
    letter-spacing: 6px;
  }
  .card--front-a .front__name { color: var(--type-grey); }
  .card--front-b .front__name { color: var(--type-light); }

  .label {
    position: absolute;
    font-family: "Cinzel", "Times New Roman", serif;
    font-size: 15px;
    letter-spacing: 3.5px;
    color: var(--label);
  }
  .label--back { left: 903px; top: 376px; }
  .label--front-a { left: 66px; top: 848px; }
  .label--front-b { left: 659px; top: 848px; }
</style>
</head>
<body>

  <section class="card card--back" aria-label="Card back">
    <svg class="back__decor" viewBox="0 0 300 300" aria-hidden="true">
      <circle cx="150" cy="150" r="140" fill="#e3e3e3" opacity="0.7"/>
    </svg>
    <div class="back__brand">
      <svg width="70" height="70" viewBox="0 0 70 70" aria-hidden="true">
        <circle cx="35" cy="35" r="30" fill="var(--silver)"/>
      </svg>
      <div class="back__brand-text">
        <span class="back__name">Marisa Kellan</span>
        <span class="back__role">fashion designer</span>
      </div>
    </div>
    <dl class="contact">
      <dt>PH</dt><dd>0412555018</dd>
      <dt>EMAIL</dt><dd>marisa@marisakellan.com</dd>
      <dt>WEB</dt><dd>www.marisakellan.com</dd>
    </dl>
  </section>
  <span class="label label--back">BACK</span>

  <section class="card card--front-a" aria-label="Card front, light version">
    <svg class="front__mark" width="180" height="180" viewBox="0 0 180 180" aria-hidden="true">
      <circle cx="90" cy="90" r="82" fill="var(--silver)"/>
    </svg>
    <div class="front__name">Marisa Kellan</div>
  </section>
  <span class="label label--front-a">FRONT A</span>

  <section class="card card--front-b" aria-label="Card front, dark version">
    <svg class="front__mark" width="180" height="180" viewBox="0 0 180 180" aria-hidden="true">
      <circle cx="90" cy="90" r="82" fill="var(--silver)"/>
    </svg>
    <div class="front__name">Marisa Kellan</div>
  </section>
  <span class="label label--front-b">FRONT B</span>

</body>
</html>
```